Business Card Design Project

Professional business cards for law firm - a rough example of what we are looking for is attached. The logo, colour and styling of the name are all new and dont need to be changed. We need layout for front and back. We are looking for some imaginative layout of info. We are a young vibrant firm and not too conservative and are not adverse to something quite different.
Updates

Thank you for all the submissions.  We have been blown away with the quality of your work.  Our management team will be meeting later in the week to make our decision.  Again, thanks for the fabulous work.

Industry/Entity Type

Conservative

Requirements
Must have
• Logo and name as in attached example (colour and font)
Should not have
• Scales of Justice

```html
<!DOCTYPE html>
<html lang="en">
<head>
<meta charset="utf-8">
<title>Marlow Reid Legal – Business Cards</title>
<link rel="stylesheet" href="https://fonts.googleapis.com/css2?family=Open+Sans:ital,wght@0,400;0,600;1,400&family=Arimo:wght@400;700&family=Tinos:ital,wght@1,700&display=swap">
<style>
  :root {
    --stage: #000000;
    --card: #ffffff;
    --green: #5f7a36;
    --green-light: #7d9150;
    --steel: #5b606d;
    --steel-light: #9a9eaa;
    --ink: #3f4046;
    --ink-soft: #55565c;
    --pill-top: #9c9d92;
    --pill-bottom: #4a4c44;
    --glow: rgba(255,255,255,0.75);
  }
  * { margin: 0; padding: 0; box-sizing: border-box; }
  html, body {
    width: 1200px; height: 1067px; overflow: hidden;
    background: var(--stage);
  }
  .stage { position: relative; width: 1200px; height: 1067px; }

  .card {
    position: absolute;
    width: 769px; height: 441px;
    background: var(--card);
    border-radius: 26px;
    overflow: hidden;
    box-shadow: 0 0 14px 4px var(--glow);
  }
  .card--front { left: 73px; top: 55px; }
  .card--back  { left: 351px; top: 538px; }

  .card__bands { position: absolute; inset: 0; width: 100%; height: 100%; }

  /* front */
  .emblem-disc {
    position: absolute; left: 131px; top: 130px;
    width: 192px; height: 192px; border-radius: 50%;
    border: 4px solid var(--steel);
  }
  .firm-name {
    position: absolute; left: 381px; top: 176px;
    font-family: "Open Sans", sans-serif; font-weight: 600;
    color: var(--green); font-size: 40px; line-height: 1.05;
  }
  .firm-name__sub { display: block; font-size: 24px; letter-spacing: 3px; margin-left: 60px; margin-top: 2px; }
  .tagline {
    position: absolute; left: 385px; top: 277px;
    font-family: "Open Sans", sans-serif; font-style: italic;
    font-size: 16px; color: var(--ink);
  }

  /* back */
  .contact {
    position: absolute; left: 45px; top: 38px;
    font-family: "Arimo", sans-serif; font-size: 20px; line-height: 25.5px;
    color: var(--ink-soft);
  }
  .contact__row { display: flex; }
  .contact__label { width: 33px; }
  .person {
    position: absolute; right: 38px; top: 38px; text-align: right;
    color: var(--ink-soft);
  }
  .person__name { font-family: "Tinos", serif; font-style: italic; font-weight: 700; font-size: 23px; }
  .person__role { font-family: "Arimo", sans-serif; font-size: 20px; margin-top: 2px; }

  .services {
    position: absolute; left: 0; right: 0; top: 204px;
    display: flex; flex-direction: column; align-items: center; gap: 15px;
    list-style: none;
  }
  .services__row { display: flex; gap: 12px; }
  .service {
    height: 27px; padding: 0 6px;
    display: flex; align-items: center; justify-content: center;
    border-radius: 6px;
    background: linear-gradient(var(--pill-top), #6b6d63 50%, var(--pill-bottom) 51%, #6e705f);
    box-shadow: 0 1px 2px rgba(0,0,0,0.5);
    font-family: "Arimo", sans-serif; font-weight: 700; font-size: 15.5px;
    color: #ffffff; text-shadow: 0 1px 1px rgba(0,0,0,0.6);
  }
</style>
</head>
<body>
<main class="stage">

  <section class="card card--front" aria-label="Card front">
    <svg class="card__bands" viewBox="0 0 769 441" preserveAspectRatio="none" aria-hidden="true">
      <defs>
        <linearGradient id="band" x1="0" x2="1" y1="0" y2="0">
          <stop offset="0" stop-color="var(--green)"/>
          <stop offset="0.3" stop-color="var(--green-light)"/>
          <stop offset="0.5" stop-color="var(--steel)"/>
          <stop offset="0.62" stop-color="var(--steel-light)"/>
          <stop offset="0.75" stop-color="var(--steel)"/>
          <stop offset="1" stop-color="var(--green)"/>
        </linearGradient>
      </defs>
      <path d="M0,0 H769 V58 C560,70 300,100 0,98 Z" fill="url(#band)"/>
      <path d="M0,120 C300,120 560,84 769,72" fill="none" stroke="var(--green)" stroke-width="6"/>
      <path d="M0,372 C300,374 560,330 769,312" fill="none" stroke="var(--steel)" stroke-width="6"/>
      <path d="M0,441 V392 C260,398 520,352 769,338 V441 Z" fill="url(#band)"/>
    </svg>
    <div class="emblem-disc"></div>
    <h1 class="firm-name">Marlow Reid<span class="firm-name__sub">LEGAL</span></h1>
    <p class="tagline">helping you find the way forward</p>
  </section>

  <section class="card card--back" aria-label="Card back">
    <svg class="card__bands" viewBox="0 0 769 441" preserveAspectRatio="none" aria-hidden="true">
      <defs>
        <linearGradient id="bandBack" x1="0" x2="1" y1="0" y2="0">
          <stop offset="0" stop-color="var(--green)"/>
          <stop offset="0.3" stop-color="var(--green-light)"/>
          <stop offset="0.5" stop-color="var(--steel)"/>
          <stop offset="0.62" stop-color="var(--steel-light)"/>
          <stop offset="0.75" stop-color="var(--steel)"/>
          <stop offset="1" stop-color="var(--green)"/>
        </linearGradient>
      </defs>
      <path d="M0,382 C300,384 560,330 769,314" fill="none" stroke="var(--green)" stroke-width="8"/>
      <path d="M0,441 V404 C260,410 520,360 769,344 V441 Z" fill="url(#bandBack)"/>
    </svg>

    <address class="contact" style="font-style:normal">
      <div class="contact__row"><span class="contact__label">T:</span><span>9400 1234</span></div>
      <div class="contact__row"><span class="contact__label"></span><span>6100 5678</span></div>
      <div class="contact__row"><span class="contact__label">F:</span><span>6300 9012</span></div>
      <div class="contact__row"><span class="contact__label">E:</span><span>hello@marlowreidlegal.com.au</span></div>
      <div class="contact__row"><span class="contact__label">H:</span><span>2/45 Harbour Street, Elmvale WA 6199</span></div>
      <div class="contact__row"><span class="contact__label"></span><span>PO Box 312, Elmvale WA 6999</span></div>
    </address>

    <div class="person">
      <p class="person__name">Clara Marlow LLB BA</p>
      <p class="person__role">Solicitor</p>
    </div>

    <ul class="services">
      <li class="services__row">
        <span class="service" style="width:135px">Family</span>
        <span class="service" style="width:135px">Traffic</span>
        <span class="service" style="width:135px">Criminal</span>
      </li>
      <li class="services__row">
        <span class="service" style="width:160px">Restraining Orders</span>
        <span class="service" style="width:150px">Probate/Wills</span>
        <span class="service" style="width:134px">Debt Recovery</span>
      </li>
      <li class="services__row">
        <span class="service" style="width:134px">Dividing Fences</span>
        <span class="service" style="width:181px">Financial Agreements</span>
      </li>
    </ul>
  </section>

</main>
</body>
</html>
```